Real Estate Business card design

Company Name: Tamarind Holdings, LLC
subtitle: We pay cash for houses!
Daniel Whitcombe
Managing Director
555-214-0963
Dan@TamarindHoldingsLLC.example
www.TamarindHoldingsLLC.example

We pay referral fees for Seller and Buyer leads.

Back:
We offer referral fees for Seller and Buyer leads that close.

Please contact Hal at 555-214-0963 with your referrals or to learn more about the referral program!

I am open to different color options but I am going for a classic, elegant, clean, and professional look. Please use logo as a reference.

Target Market(s)

People selling their homes and people in the market for buying homes.

Contact Information for Business Card

please see project description

Font styles to use
Serif
Sans Serif
Script

Requirements
Must have
• must have my logo in it
Nice to have
• I like cards that are split down the middle but please come up with a few mock ups. Open to any color scheme.

```html
<!DOCTYPE html>
<html lang="en">
<head>
<meta charset="utf-8">
<title>Tamarind Holdings, LLC – Business Card</title>
<link href="https://fonts.googleapis.com/css2?family=Montserrat:wght@400;500;600;700&display=swap" rel="stylesheet">
<style>
  :root {
    --bg: #2f343d;
    --slate: #3a3f4a;
    --paper: #f2f1f1;
    --gold: #c1935f;
    --ink: #2b2f36;
    --white: #ffffff;
  }
  * { margin: 0; padding: 0; box-sizing: border-box; }
  html, body { width: 1200px; height: 502px; overflow: hidden; }
  body {
    background: var(--bg);
    font-family: "Montserrat", sans-serif;
    display: flex;
    align-items: center;
    justify-content: center;
    gap: 40px;
  }
  .card {
    position: relative;
    width: 540px;
    height: 307px;
    background: var(--paper);
    overflow: hidden;
  }
  .card-shapes { position: absolute; inset: 0; width: 100%; height: 100%; }

  /* Front */
  .holder-name {
    position: absolute;
    left: 45px; top: 34px;
    color: var(--gold);
    font-weight: 700;
    font-size: 21px;
    line-height: 1.2;
    letter-spacing: 0.8px;
    text-transform: uppercase;
  }
  .brand {
    position: absolute;
    left: 300px; top: 70px;
    width: 220px;
    display: flex;
    align-items: center;
    gap: 10px;
  }
  .brand-mark { width: 14px; height: 14px; background: var(--gold); flex: none; }
  .brand-name {
    color: var(--white);
    font-weight: 600;
    font-size: 24px;
    line-height: 1.1;
  }
  .tagline {
    position: absolute;
    right: 38px; top: 173px;
    color: var(--gold);
    font-weight: 600;
    font-size: 11.5px;
    letter-spacing: 2.4px;
  }
  .contact-list {
    position: absolute;
    left: 45px; top: 220px;
    list-style: none;
    color: var(--white);
    font-size: 15px;
  }
  .contact-list li { display: flex; align-items: center; gap: 10px; height: 24px; }
  .contact-icon { width: 15px; height: 15px; flex: none; }

  /* Back */
  .referral {
    position: absolute;
    left: 0; right: 0; top: 42px;
    text-align: center;
    color: var(--ink);
    font-size: 15.5px;
    line-height: 1.42;
  }
  .referral p + p { margin-top: 20px; }
  .referral strong { font-weight: 500; font-size: 17px; }
  .inline-phone { width: 13px; height: 13px; vertical-align: -1px; margin-right: 2px; }
  .back-brand {
    position: absolute;
    left: 0; right: 0; bottom: 26px;
    display: flex;
    justify-content: center;
    align-items: center;
    gap: 10px;
  }
  .back-brand .brand-name { color: var(--gold); font-size: 18px; }
</style>
</head>
<body>

  <section class="card card-front" aria-label="Business card front">
    <svg class="card-shapes" viewBox="0 0 540 307" preserveAspectRatio="none" aria-hidden="true">
      <polygon points="340,0 540,0 540,307 0,307 0,224" fill="var(--slate)"/>
      <polygon points="334,0 340,0 0,224 0,220" fill="var(--gold)"/>
    </svg>

    <h1 class="holder-name">Daniel<br>Whitcombe</h1>

    <div class="brand">
      <span class="brand-mark"></span>
      <span class="brand-name">Tamarind<br>Holdings, LLC</span>
    </div>
    <p class="tagline">We pay cash for houses!</p>

    <ul class="contact-list">
      <li>
        <svg class="contact-icon" viewBox="0 0 24 24" fill="var(--gold)" aria-hidden="true"><path d="M6.6 10.8a15.1 15.1 0 0 0 6.6 6.6l2.2-2.2a1 1 0 0 1 1-.25 11.4 11.4 0 0 0 3.6.57 1 1 0 0 1 1 1V20a1 1 0 0 1-1 1A17 17 0 0 1 3 4a1 1 0 0 1 1-1h3.5a1 1 0 0 1 1 1c0 1.250.2 2.45.57 3.57a1 1 0 0 1-.25 1z"/></svg>
        555-214-0963
      </li>
      <li>
        <svg class="contact-icon" viewBox="0 0 24 24" fill="var(--gold)" aria-hidden="true"><path d="M3 5h18v14H3z" opacity=".9"/><path d="M3 5l9 7 9-7" fill="none" stroke="var(--slate)" stroke-width="1.8"/></svg>
        Dan@TamarindHoldingsLLC.example
      </li>
      <li>
        <svg class="contact-icon" viewBox="0 0 24 24" fill="none" stroke="var(--gold)" stroke-width="2" aria-hidden="true"><circle cx="12" cy="12" r="9"/><path d="M3 12h18M12 3c3 3 3 15 0 18M12 3c-3 3-3 15 0 18"/></svg>
        www.TamarindHoldingsLLC.example
      </li>
    </ul>
  </section>

  <section class="card card-back" aria-label="Business card back">
    <div class="referral">
      <p>We offer referral fees for Seller<br>and Buyer leads that close.</p>
      <p>Please contact <strong>HAL</strong> at
        <svg class="inline-phone" viewBox="0 0 24 24" fill="var(--gold)" aria-hidden="true"><path d="M6.6 10.8a15.1 15.1 0 0 0 6.6 6.6l2.2-2.2a1 1 0 0 1 1-.25 11.4 11.4 0 0 0 3.6.57 1 1 0 0 1 1 1V20a1 1 0 0 1-1 1A17 17 0 0 1 3 4a1 1 0 0 1 1-1h3.5a1 1 0 0 1 1 1c0 1.25.2 2.45.57 3.57a1 1 0 0 1-.25 1z"/></svg>555-214-0963<br>with your referrals or to learn more about<br>the referral program!</p>
    </div>
    <div class="back-brand">
      <span class="brand-mark"></span>
      <span class="brand-name">Tamarind Holdings, LLC</span>
    </div>
  </section>

</body>
</html>
```